Flyer for American Indian Elders on Dementia Warning Signs

We need a flyer designed for older adults who are American Indian or Alaska Native (in the U.S.).

Ideally, the flyer should complement the colors of our logos. The project logo and our organization logo are attached to the brief.

When people see the flyer we want them to feel that it represents their culture, is warm, and professional but relatable to older adults and people who have limited incomes.

I have attached an earlier draft of the document we designed ourselves BUT we want different and better.

It is for older adults who have trouble reading so:
1. you must use a font that is 11.5 points or larger
2. Do not put text over complex pictures or use shading with words
3. You can use a serif font for the heading, but should use san serif for the body text
4. There should be good contrast between the font color and background

Please do not use any images that include a head dress or pictures of American Indian people or things that are very traditional or "token" imagery.

We need to save a small space under the call out box/ somewhere on the flyer for other people to add their logo once they download.

Let us know if you have questions or need additional information.

Target Market(s)

Older American Indian people

Font styles to use
Serif
Sans Serif

Requirements
Must have
• Easy to read for older adults
Should not have
• indian headdress

```html
<!DOCTYPE html>
<html lang="en">
<head>
<meta charset="utf-8">
<title>10 Signs of Thinking or Memory Changes That Might Be Dementia</title>
<link href="https://fonts.googleapis.com/css2?family=Bebas+Neue&family=Open+Sans:wght@400;600;700&display=swap" rel="stylesheet">
<style>
  :root {
    --teal: #5aabb2;
    --teal-deep: #4d9ea6;
    --slate: #7d8c8d;
    --clay: #b05d56;
    --clay-box: #b1625b;
    --white: #ffffff;
    --ink: #1f1f1f;
  }
  * { margin: 0; padding: 0; box-sizing: border-box; }
  html, body { width: 927px; height: 1200px; overflow: hidden; background: var(--white); }
  .flyer {
    position: relative;
    width: 927px;
    height: 1200px;
    overflow: hidden;
    font-family: "Open Sans", sans-serif;
    background: var(--white);
  }
  .backdrop { position: absolute; inset: 0; }

  .title {
    position: absolute;
    left: 0; top: 28px;
    width: 425px;
    text-align: center;
    white-space: nowrap;
    font-family: "Bebas Neue", sans-serif;
    font-weight: 400;
    font-size: 56px;
    line-height: 77px;
    letter-spacing: 0.5px;
    color: var(--white);
  }

  .intro {
    position: absolute;
    left: 21px; top: 387px;
    width: 380px;
    font-size: 16px;
    line-height: 22.8px;
    letter-spacing: 0.5px;
    color: var(--ink);
    white-space: nowrap;
  }
  .intro p + p { margin-top: 22.8px; }

  .main-points {
    position: absolute;
    left: 12px; top: 685px;
    width: 379px; height: 355px;
    background: var(--clay-box);
    border-radius: 4px;
    padding: 13px 10px 0 13px;
    color: var(--white);
    font-size: 16.2px;
    line-height: 22.8px;
    letter-spacing: 0.4px;
    white-space: nowrap;
  }
  .main-points h2 {
    font-size: 19.5px;
    font-weight: 700;
    line-height: 24px;
    letter-spacing: 0.3px;
  }
  .main-points p + p { margin-top: 22.8px; }

  .partner-mark {
    position: absolute;
    left: 24px; top: 1090px;
    display: flex; align-items: center; gap: 10px;
    font-size: 16px;
    font-weight: 700;
    line-height: 20px;
    color: var(--teal-deep);
  }
  .partner-mark .dot { width: 26px; height: 26px; border-radius: 50%; background: var(--teal-deep); flex: none; }

  .center-mark {
    position: absolute;
    left: 556px; top: 34px;
    display: flex; align-items: center; gap: 14px;
  }
  .center-mark .dot { width: 86px; height: 86px; border-radius: 50%; background: var(--teal); flex: none; }
  .center-mark .name {
    font-size: 22px;
    font-weight: 700;
    line-height: 26px;
    color: var(--teal-deep);
    width: 240px;
  }

  .sign {
    position: absolute;
    left: 484px;
    width: 436px;
    font-size: 15.4px;
    line-height: 20.9px;
    letter-spacing: 0.35px;
    color: var(--white);
    white-space: nowrap;
  }
  .sign ul { list-style: none; }
  .sign li::before { content: "\2022\00a0"; }
</style>
</head>
<body>
<div class="flyer">
  <svg class="backdrop" width="927" height="1200" viewBox="0 0 927 1200" aria-hidden="true">
    <defs>
      <linearGradient id="column-fade" x1="0" y1="0" x2="0" y2="1">
        <stop offset="0" stop-color="#5aabb2"/>
        <stop offset="0.38" stop-color="#7d8c8d"/>
        <stop offset="0.62" stop-color="#b05d56"/>
        <stop offset="1" stop-color="#b05d56"/>
      </linearGradient>
    </defs>
    <path d="M0 17 C150 14 330 14 420 24 C470 32 500 80 530 112 C548 132 565 140 600 140 L927 140 L927 1200 L0 1200 Z" fill="url(#column-fade)"/>
    <path d="M0 360 L265 360 C350 360 405 430 405 530 L405 1200 L0 1200 Z" fill="#ffffff"/>
  </svg>

  <h1 class="title">10 Signs of<br>Thinking or Memory<br>Changes That Might<br>Be Dementia</h1>

  <div class="center-mark">
    <span class="dot"></span>
    <span class="name">Cedar Ridge Brain Health Center</span>
  </div>

  <div class="intro">
    <p>As we get older, we may slow down<br>a bit. This is a normal part of aging.<br>Changes in memory or thinking that<br>make it harder to get through the day,<br>are not a normal part of aging.<br>These may be early signs of dementia.</p>
    <p>Because American Indian and Alaska Native<br>people have a high risk of dementia,<br>it is important to know the warning signs.<br>Do you have any of these 10 signs?<br>If so, talk to your doctor.</p>
  </div>

  <section class="main-points">
    <h2>Main Points</h2>
    <p>American Indian and Alaska Native people<br>have a high risk of dementia.</p>
    <p>Big changes in memory or thinking that<br>make it hard to get through the day are not<br>a normal part of aging.</p>
    <p>People with one or more of these 10 signs<br>should talk to their doctor to find the<br>cause. It is not always dementia.</p>
    <p>Early dementia diagnosis gives you a<br>chance to get care and plan your future.</p>
  </section>

  <div class="partner-mark">
    <span class="dot"></span>
    <span>Riverstone<br>Elders Network</span>
  </div>

  <div class="sign" style="top:182px">1. Memory loss that affects your daily life. You may:
    <ul><li>Forget events or important dates</li><li>Repeat yourself</li><li>Rely more often on lists or sticky notes to<br>remember things</li></ul></div>

  <div class="sign" style="top:307px">2. Sudden trouble planning or solving problems.<br>You may have a harder time:
    <ul><li>Paying bills</li><li>Cooking recipes you have used for years</li></ul></div>

  <div class="sign" style="top:412px">3. You get confused about the time, date,<br>or where you are.</div>

  <div class="sign" style="top:475px">4. Daily tasks are getting harder, including:
    <ul><li>Driving</li><li>Making a grocery list or going shopping</li></ul></div>

  <div class="sign" style="top:558px">5. Trouble with how your eyesight and thinking work<br>together that gets worse. This includes:
    <ul><li>Tripping, falls, or problems with your balance</li><li>Spilling or dropping things more</li></ul></div>

  <div class="sign" style="top:663px">6. New trouble talking or writing. You have a hard<br>time finding the words you want to say. For example,<br>you may say “that thing on your wrist that tells time”<br>instead of “watch.”</div>

  <div class="sign" style="top:767px">7. You lose and cannot find things. For example, you:
    <ul><li>Can’t find the coffee pot that you use every day</li><li>Might put your car keys in the freezer</li></ul></div>

  <div class="sign" style="top:851px">8. Notice changes in your mood or personality,<br>such as being:
    <ul><li>Easily mad or sad in everyday situations</li><li>More fearful (scared) or suspicious (not trusting)</li></ul></div>

  <div class="sign" style="top:955px">9. Act different and act without thinking. Make poor<br>choices. This may make you more likely to:
    <ul><li>Spend money you do not have or be a scam victim</li><li>Stop washing up regularly or pay less attention<br>to how you look</li><li>Forget to take care of your pet</li></ul></div>

  <div class="sign" style="top:1102px">10. Pull away from friends and family because it is harder<br>to keep up. You may not want to do things you used to<br>enjoy, like sporting events, church, music, or sex.</div>
</div>
</body>
</html>
```